Carpet cleaning company focused on high quality needs business cards

We are a growing company that just merged with another company and need to design a new business card. We do both residential as well as commercial cleaning. We do carpet, tile & grout, upholstery, hard floors, and stain & pet odor removal. We treat our customers like family and strive to achieve outstanding results with every job.

```html
<!DOCTYPE html>
<html lang="en">
<head>
<meta charset="utf-8">
<title>Vera's Vapor Crew Cleaning – Business Card</title>
<link rel="stylesheet" href="https://fonts.googleapis.com/css2?family=Poppins:wght@400;600;800&display=swap">
<style>
  :root {
    --stage: #2b2b2d;
    --card-white: #ffffff;
    --card-black: #151617;
    --ink: #1a1a1a;
    --accent: #e8433f;
    --link-blue: #1f3b5c;
    --line-soft: #f0a6a3;
  }
  * { box-sizing: border-box; margin: 0; padding: 0; }
  html, body { width: 1200px; height: 1108px; overflow: hidden; }
  body {
    background: var(--stage);
    font-family: "Poppins", sans-serif;
    display: flex;
    align-items: center;
    justify-content: center;
    gap: 80px;
  }
  .card {
    width: 360px;
    height: 600px;
    border-radius: 22px;
    position: relative;
    overflow: hidden;
  }

  /* Front */
  .card-front {
    background: var(--card-white);
    color: var(--ink);
    display: flex;
    flex-direction: column;
    align-items: center;
    padding: 70px 34px 40px;
  }
  .brand-lockup {
    display: flex;
    align-items: center;
    gap: 14px;
    width: 100%;
  }
  .mascot-art {
    width: 140px;
    height: 160px;
    border-radius: 4px;
    background: linear-gradient(160deg, #3f7fc1 0%, #c9a36b 55%, var(--accent) 100%);
    flex-shrink: 0;
  }
  .brand-name {
    font-weight: 800;
    font-size: 26px;
    line-height: 1.08;
    color: var(--ink);
    text-transform: uppercase;
  }
  .person {
    margin-top: 80px;
    text-align: center;
  }
  .person-name {
    color: var(--accent);
    font-weight: 600;
    font-size: 23px;
    letter-spacing: 0.5px;
    text-transform: uppercase;
    line-height: 1.2;
  }
  .person-title {
    font-size: 16px;
    color: var(--ink);
  }
  .icon-row {
    margin-top: 14px;
    width: 100%;
    display: flex;
    align-items: center;
    gap: 8px;
  }
  .icon-row .rule { flex: 1; height: 1px; background: var(--line-soft); }
  .icon-tile {
    width: 24px; height: 24px;
    background: var(--accent);
    border-radius: 4px;
    display: flex; align-items: center; justify-content: center;
  }
  .contact-list {
    margin-top: 10px;
    text-align: center;
    font-size: 16px;
    line-height: 1.5;
    list-style: none;
  }
  .contact-list .web { color: var(--link-blue); }
  .divider { width: 82%; height: 1px; background: var(--line-soft); margin: 10px 0; }
  .address { text-align: center; font-size: 16px; line-height: 1.45; font-style: normal; }

  /* Back */
  .card-back {
    background: var(--card-black);
    color: #fff;
  }
  .back-texture {
    position: absolute; inset: 0;
    background: radial-gradient(ellipse at 60% 40%, #242526 0%, var(--card-black) 70%);
  }
  .back-brand {
    position: absolute;
    top: 250px;
    left: 0; right: 0;
    text-align: center;
    font-weight: 800;
    font-size: 24px;
    line-height: 1.05;
    text-transform: uppercase;
    color: #fff;
  }
  .services {
    position: absolute;
    left: 20px; right: 20px;
    bottom: 72px;
    text-align: center;
  }
  .services-heading {
    font-size: 15px;
    font-weight: 400;
    letter-spacing: 0.6px;
    text-transform: uppercase;
  }
  .services-rule {
    width: 60px; height: 1px;
    background: var(--accent);
    margin: 14px auto;
  }
  .services-list {
    font-size: 15px;
    line-height: 1.75;
    color: #f3f3f3;
  }
  .dot {
    display: inline-block;
    width: 8px; height: 8px;
    border-radius: 50%;
    background: var(--accent);
    margin: 0 6px;
    vertical-align: middle;
  }
</style>
</head>
<body>

<section class="card card-front" aria-label="Business card front">
  <div class="brand-lockup">
    <div class="mascot-art" role="img" aria-label="Illustration of a cheerful cleaning technician holding a steam wand over a red panel"></div>
    <div class="brand-name">Vera's<br>Vapor<br>Crew<br>Cleaning</div>
  </div>

  <div class="person">
    <h1 class="person-name">Marcus Delaney</h1>
    <p class="person-title">Managing Director</p>
  </div>

  <div class="icon-row">
    <span class="rule"></span>
    <span class="icon-tile">
      <svg width="14" height="14" viewBox="0 0 24 24" fill="#fff" aria-hidden="true"><path d="M6.6 10.8a15 15 0 0 0 6.6 6.6l2.2-2.2a1 1 0 0 1 1-.25 11.4 11.4 0 0 0 3.6.57 1 1 0 0 1 1 1V20a1 1 0 0 1-1 1A17 17 0 0 1 3 4a1 1 0 0 1 1-1h3.5a1 1 0 0 1 1 1c0 1.25.2 2.45.57 3.57a1 1 0 0 1-.25 1z"/></svg>
    </span>
    <span class="icon-tile">
      <svg width="14" height="14" viewBox="0 0 24 24" fill="none" stroke="#fff" stroke-width="2" aria-hidden="true"><rect x="3" y="5" width="18" height="14" rx="1"/><path d="M3 6l9 7 9-7"/></svg>
    </span>
    <span class="icon-tile">
      <svg width="14" height="14" viewBox="0 0 24 24" fill="none" stroke="#fff" stroke-width="2" aria-hidden="true"><circle cx="12" cy="12" r="9"/><path d="M3 12h18M12 3c3 3 3 15 0 18M12 3c-3 3-3 15 0 18"/></svg>
    </span>
    <span class="rule"></span>
  </div>

  <ul class="contact-list">
    <li>055-987 321 640</li>
    <li>hello@vaporcrew.com</li>
    <li>www.<span class="web">vaporcrewpro</span>.com</li>
  </ul>
  <div class="divider"></div>
  <address class="address">87, Harbor Lane East<br>Eastland City, 30917</address>
</section>

<section class="card card-back" aria-label="Business card back">
  <div class="back-texture" role="img" aria-label="Subtle gloss pattern on black"></div>
  <div class="back-brand">Vera's<br>Vapor Crew<br>Cleaning</div>
  <div class="services">
    <h2 class="services-heading">Residential &amp; Commercial Cleaning.</h2>
    <div class="services-rule"></div>
    <p class="services-list">
      Carpet<span class="dot"></span>Tile &amp; Grout<span class="dot"></span>Upholstery<br>
      Hard floors &amp; Stain<span class="dot"></span>Pet Odor Removal.
    </p>
  </div>
</section>

</body>
</html>
```